依頼詳細
お好み焼き屋さんのTOPページのみのデザインをお願いしたいです。
コロナで減少したお客様を呼び戻すために試行錯誤しながら、このたびラーメンも提供することになりましたので、メインはお好み焼き屋さんですが、ラーメンも始めました!という画像付きで告知したいです。

集客を目的としたサイトです。
ターゲットは。お腹が空いた人になります!

レイアウト構成
・ヘッダー(ロゴのみ)
・TOP画像(画像はまだないのでフリーのもので大丈夫です)
・TOPページは画像だけでなくインパクトある感じを希望です(ザックリですみません。)
・お知らせ(3行程度)
・メニュー(テキストのみ)
・店舗情報(2店舗)テキスト
・フッター(下層ページないのでコピーライトぐらいでしょうか)
という構成です。
どこかにツマミドリと味ノートにリンクするボタンが欲しいです。
まだ素材がないため仮のフリー画像で構いません。

初心者の方でも大丈夫です!
今回は予算の都合上、低価格になってしまいましたがデザインのフィーリングが合う方は今後もご依頼する可能性があります!
サイトURL
ページ数
1ページ
希望イメージ
シンプル 複雑
単色 カラフル
暗い 明るい
日常 高級
遊び心 厳粛
未来的 伝統的
女性的 男性的
希望する色
無彩色系
納品ファイル
• 高解像度JPG (.jpg)
• イラストレーター形式 (.ai)
• フォトショップ形式 (.psd)
• PNG形式 (.png)
補足説明
納品はできれば、XDが希望です。
難しい場合はご相談ください。

お客様のイメージに一番近かったため選びました!

この度は、とても素晴らしいデザインのご提案をいただきまして誠にありがとうございました。
どれも捨てがたいデザインなのですが、一番イメージに近いものを選びました。
また、機会がございましたら、ご依頼をさせていただければと思います。
どうぞよろしくお願いいたします。

```html
<!DOCTYPE html>
<html lang="ja">
<head>
<meta charset="utf-8">
<title>お好み焼き TOP</title>
<link rel="stylesheet" href="https://fonts.googleapis.com/css2?family=Noto+Serif+JP:wght@400;600;700&family=Cormorant+Garamond:wght@400;500&display=swap">
<style>
:root{
  --paper:#efefed;
  --paper-dark:#e4e4e1;
  --ink:#1a1a1a;
  --ink-soft:#555;
  --white:#ffffff;
  --ghost:#cfcfcb;
  --line:#9a9a9a;
}
*{margin:0;padding:0;box-sizing:border-box}
html,body{width:1200px;height:2784px;overflow:hidden}
body{background:linear-gradient(160deg,var(--paper) 0%,var(--paper-dark) 50%,var(--paper) 100%);font-family:"Noto Serif JP",serif;color:var(--ink);position:relative}

.hero{position:absolute;left:0;top:0;width:1200px;height:660px;overflow:hidden}
.hero-photo{position:absolute;left:-60px;top:-200px;width:1320px;height:860px;border-radius:0 0 50% 50%/0 0 34% 34%;
  background:radial-gradient(ellipse at 45% 72%,#a86a34 0%,#6b4526 25%,#2e2a27 55%,#141414 85%)}
.logo{position:absolute;left:40px;top:20px;width:110px;height:110px;border-radius:50%;background:var(--white);display:flex;align-items:center;justify-content:center;font-size:34px;font-weight:700;color:var(--ink)}
.scroll{position:absolute;left:600px;top:500px;transform:translateX(-50%);text-align:center;color:var(--white);font-family:"Cormorant Garamond",serif;font-size:16px;letter-spacing:.1em}
.scroll::before{content:"";display:block;width:1px;height:90px;background:var(--white);margin:0 auto 12px}

.section-label{position:absolute;left:80px}
.section-label .en{font-family:"Cormorant Garamond",serif;font-size:96px;line-height:1;color:transparent;-webkit-text-stroke:1.5px var(--ghost);letter-spacing:.08em}
.section-label .ja{font-size:24px;font-weight:600;margin:-18px 0 0 80px}

.menu-board{position:absolute;left:152px;top:772px;width:896px;height:580px;background:var(--white);border-left:40px solid var(--ink);border-right:40px solid var(--ink);box-shadow:0 6px 18px rgba(0,0,0,.15);padding:40px 44px;display:flex;flex-direction:column;gap:40px}
.menu-row{display:flex;flex-direction:row-reverse;justify-content:space-between;align-items:flex-start;height:230px}
.menu-title{writing-mode:vertical-rl;white-space:nowrap;font-size:22px;font-weight:700;letter-spacing:.15em;padding:12px 8px;border-right:5px solid var(--ink);border-top:2px solid var(--ink)}
.menu-item{display:flex;flex-direction:column;align-items:center;gap:26px;font-size:15px;letter-spacing:.12em}
.menu-item span{writing-mode:vertical-rl;white-space:nowrap}

.news-list{position:absolute;left:160px;top:1568px;width:880px;list-style:none;border-top:1px solid var(--line)}
.news-list li{display:flex;align-items:center;gap:28px;height:38px;border-bottom:1px solid var(--line);font-size:14px}
.news-tag{background:var(--ink);color:var(--white);font-size:12px;padding:4px 14px}
.news-date{width:110px;color:var(--ink-soft)}

.branches{position:absolute;left:328px;top:1928px;display:flex;gap:40px}
.branch{width:252px}
.branch-head{height:232px;padding:28px 20px;color:var(--white);background:linear-gradient(180deg,#2b3238 0%,#3d3a35 60%,#1e1e1e 100%);position:relative}
.branch-head h3{font-size:28px;font-weight:700;text-align:center;margin-bottom:22px}
.branch-head p{font-size:12px;line-height:1.8}
.branch-head .hours{margin-top:14px}
.branch-map{height:288px;background:linear-gradient(135deg,#e9ecef,#dfe5e9 50%,#eef0ee)}

.listing-links{position:absolute;left:340px;top:2512px;display:flex;gap:40px}
.listing-btn{width:240px;height:80px;background:var(--white);display:flex;align-items:center;justify-content:center;gap:12px;font-size:24px;font-weight:700;color:var(--ink);border:1px solid #ddd}
.listing-btn i{width:14px;height:14px;background:var(--ink);display:block}

.go-top{position:absolute;left:1020px;top:2544px;text-align:center;font-family:"Cormorant Garamond",serif;font-size:14px;width:80px}
.footer{position:absolute;left:0;top:2640px;width:1200px;height:144px;background:#000;color:var(--white);display:flex;align-items:center;justify-content:center;font-size:14px}
</style>
</head>
<body>
<header class="hero">
  <div class="hero-photo" role="img" aria-label="鉄板の上で焼かれるお好み焼きとヘラを持つ手"></div>
  <div class="logo">ロゴ</div>
  <div class="scroll">scroll</div>
</header>

<div class="section-label" style="top:650px"><div class="en">Menu</div><div class="ja">お品書き</div></div>
<section class="menu-board">
  <div class="menu-row">
    <div class="menu-title">お好み焼き</div>
    <div class="menu-item"><span>お好み焼き</span><span>５００円</span></div>
    <div class="menu-item"><span>お好み焼き</span><span>５００円</span></div>
    <div class="menu-item"><span>お好み焼き</span><span>５００円</span></div>
    <div class="menu-item"><span>お好み焼き</span><span>５００円</span></div>
    <div class="menu-item"><span>お好み焼き</span><span>５００円</span></div>
    <div class="menu-item"><span>お好み焼き</span><span>５００円</span></div>
    <div class="menu-item"><span>お好み焼き</span><span>５００円</span></div>
  </div>
  <div class="menu-row">
    <div class="menu-title">もんじゃ焼き</div>
    <div class="menu-item"><span>もんじゃ焼き</span><span>５００円</span></div>
    <div class="menu-item"><span>もんじゃ焼き</span><span>５００円</span></div>
    <div class="menu-item"><span>もんじゃ焼き</span><span>５００円</span></div>
    <div class="menu-title">お好み焼き</div>
    <div class="menu-item"><span>お好み焼き</span><span>５００円</span></div>
    <div class="menu-item"><span>お好み焼き</span><span>５００円</span></div>
    <div class="menu-item"><span>お好み焼き</span><span>５００円</span></div>
    <div class="menu-item"><span>お好み焼き</span><span>５００円</span></div>
  </div>
</section>

<div class="section-label" style="top:1430px"><div class="en">News</div><div class="ja">お知らせ</div></div>
<ul class="news-list">
  <li><span class="news-tag">お知らせ</span><span class="news-date">2023.2.14</span><span>お知らせテキストが入ります。お知らせテキストが入ります。お知らせテキストが入ります。</span></li>
  <li><span class="news-tag">お知らせ</span><span class="news-date">2023.2.14</span><span>お知らせテキストが入ります。お知らせテキストが入ります。お知らせテキストが入ります。</span></li>
  <li><span class="news-tag">お知らせ</span><span class="news-date">2023.2.14</span><span>お知らせテキストが入ります。お知らせテキストが入ります。お知らせテキストが入ります。</span></li>
</ul>

<div class="section-label" style="top:1790px"><div class="en">Branch</div><div class="ja">店舗一覧</div></div>
<section class="branches">
  <article class="branch">
    <div class="branch-head">
      <h3>支店 1号店</h3>
      <p>東京都緑ヶ丘区花町1-2-3<br>03-0000-0000</p>
      <p class="hours">営業時間　11:00-23:00</p>
    </div>
    <div class="branch-map" role="img" aria-label="1号店周辺の地図"></div>
  </article>
  <article class="branch">
    <div class="branch-head">
      <h3>支店 2号店</h3>
      <p>東京都緑ヶ丘区花町4-5-6<br>03-0000-0000</p>
      <p class="hours">営業時間　11:00-23:00</p>
    </div>
    <div class="branch-map" role="img" aria-label="2号店周辺の地図"></div>
  </article>
</section>

<nav class="listing-links">
  <a class="listing-btn"><i></i>ツマミドリ</a>
  <a class="listing-btn"><i></i>味ノート</a>
</nav>

<div class="go-top">
  <svg width="24" height="14" viewBox="0 0 24 14"><path d="M2 12 L12 2 L22 12" fill="none" stroke="#1a1a1a" stroke-width="1.5"/></svg>
  <div>Go to Top</div>
</div>

<footer class="footer">Copyright © Teppan Hana 2023.</footer>
</body>
</html>
```